we are plumbers and builders.

one side with vellmore installations dean hartfield 07823415067 01632960418 info@vellmoreinstallations.co.uk
other side
vellmore construction
luke hartfield 07700914372
01632960418
info@vellmoreconstruction.co.uk

i don't want your bog standard logo id like something unusual maybe shape the card. i like black and silver,

```html
<!DOCTYPE html>
<html lang="en">
<head>
<meta charset="utf-8">
<title>Vellmore Business Cards</title>
<link rel="stylesheet" href="https://fonts.googleapis.com/css2?family=Poppins:wght@400;500;800&display=swap">
<style>
  :root {
    --backdrop: #141414;
    --card-top: #1c1c1c;
    --card-bottom: #0b0b0b;
    --red: #e3222a;
    --silver: #c9c9c9;
    --silver-dim: #9a9a9a;
  }
  * { box-sizing: border-box; margin: 0; padding: 0; }
  html, body { width: 1200px; height: 1200px; overflow: hidden; }
  body {
    background: var(--backdrop);
    font-family: "Poppins", sans-serif;
    position: relative;
  }
  .card {
    position: absolute;
    left: 150px;
    width: 900px;
    height: 527px;
    border-radius: 8px 40px 8px 40px;
    background: linear-gradient(150deg, var(--card-top), var(--card-bottom) 70%);
    overflow: hidden;
    box-shadow: 0 24px 50px rgba(0,0,0,0.6);
  }
  .card--installations { top: 50px; }
  .card--construction { top: 620px; }

  .brand {
    position: absolute;
    display: flex;
    align-items: center;
    gap: 24px;
  }
  .brand__mark {
    width: 26px;
    height: 26px;
    background: var(--silver-dim);
    flex: none;
  }
  .brand__name {
    font-weight: 500;
    color: var(--red);
    line-height: 1.1;
    letter-spacing: 0.04em;
    text-transform: uppercase;
    white-space: nowrap;
  }
  .card--installations .brand { left: 190px; top: 80px; }
  .card--installations .brand__name { font-size: 46px; }
  .card--construction .brand { left: 190px; top: 80px; }
  .card--construction .brand__name { font-size: 54px; }

  .person {
    font-weight: 800;
    color: var(--red);
    text-transform: uppercase;
    letter-spacing: 0.02em;
    white-space: nowrap;
  }
  .contacts { list-style: none; color: var(--silver); white-space: nowrap; }
  .contacts li { display: flex; align-items: center; gap: 8px; line-height: 1.3; }
  .contacts svg { flex: none; }

  .card--installations .details { position: absolute; left: 90px; top: 280px; }
  .card--installations .person { font-size: 26px; margin-bottom: 6px; }
  .card--installations .contacts { font-size: 22px; }

  .card--construction .details {
    position: absolute;
    left: 70px;
    top: 320px;
    display: flex;
    align-items: center;
  }
  .card--construction .person { font-size: 30px; padding-right: 30px; }
  .divider { width: 2px; height: 96px; background: var(--silver-dim); margin-right: 30px; flex: none; }
  .card--construction .contacts { font-size: 24px; }
</style>
</head>
<body>
  <section class="card card--installations">
    <div class="brand">
      <span class="brand__mark" aria-hidden="true"></span>
      <span class="brand__name">Vellmore<br>Installations</span>
    </div>
    <div class="details">
      <p class="person">Dean Hartfield</p>
      <ul class="contacts">
        <li><svg width="20" height="20" viewBox="0 0 20 20" aria-hidden="true"><circle cx="10" cy="10" r="8" fill="none" stroke="#c9c9c9" stroke-width="2"/><path d="M7 6c-1 1 0 4 2 6s4 3 5 2l-1.5-1.5-1.2.8C10 12.5 8 10.5 7.5 9.2l.8-1.2z" fill="#e3222a"/></svg>07823415067</li>
        <li><svg width="20" height="20" viewBox="0 0 20 20" aria-hidden="true"><circle cx="10" cy="10" r="8" fill="none" stroke="#c9c9c9" stroke-width="2"/><path d="M7 6c-1 1 0 4 2 6s4 3 5 2l-1.5-1.5-1.2.8C10 12.5 8 10.5 7.5 9.2l.8-1.2z" fill="#e3222a"/></svg>01632960418</li>
        <li><svg width="20" height="20" viewBox="0 0 20 20" aria-hidden="true"><circle cx="10" cy="10" r="8" fill="none" stroke="#c9c9c9" stroke-width="2"/><rect x="6" y="7" width="8" height="6" fill="#e3222a"/></svg>info@vellmoreinstallations.co.uk</li>
      </ul>
    </div>
  </section>

  <section class="card card--construction">
    <div class="brand">
      <span class="brand__mark" aria-hidden="true"></span>
      <span class="brand__name">Vellmore<br>Construction</span>
    </div>
    <div class="details">
      <p class="person">Luke Hartfield</p>
      <span class="divider" aria-hidden="true"></span>
      <ul class="contacts">
        <li><svg width="22" height="22" viewBox="0 0 20 20" aria-hidden="true"><circle cx="10" cy="10" r="8" fill="none" stroke="#c9c9c9" stroke-width="2"/><path d="M7 6c-1 1 0 4 2 6s4 3 5 2l-1.5-1.5-1.2.8C10 12.5 8 10.5 7.5 9.2l.8-1.2z" fill="#e3222a"/></svg>07700914372</li>
        <li><svg width="22" height="22" viewBox="0 0 20 20" aria-hidden="true"><circle cx="10" cy="10" r="8" fill="none" stroke="#c9c9c9" stroke-width="2"/><path d="M7 6c-1 1 0 4 2 6s4 3 5 2l-1.5-1.5-1.2.8C10 12.5 8 10.5 7.5 9.2l.8-1.2z" fill="#e3222a"/></svg>01632960418</li>
        <li><svg width="22" height="22" viewBox="0 0 20 20" aria-hidden="true"><circle cx="10" cy="10" r="8" fill="none" stroke="#c9c9c9" stroke-width="2"/><rect x="6" y="7" width="8" height="6" fill="#e3222a"/></svg>info@vellmoreconstruction.co.uk</li>
      </ul>
    </div>
  </section>
</body>
</html>
```